Direct Mail Marketing Postcard Template Design

Mine is a residential real estate marketing service for "Fixer Upper" properties in Central Indiana. My company owns the properties being promoted on a proprietary/branded web site (also being developed by Corvel Press) and by Direct Mail . The properties for sale are not traditional real estate "listings".

I expect the post card and the web site to establish and promote the "new" brand for Bramble Arc Holdings, Inc.

The post card will be mailed to specific niche markets; primarily "Hands On" real estate investors, Rehabbers, Landlords, and First Time Home Buyers. The cards will routinely be mailed to investors and to residents in the area surrounding a property for sale to generate home buyer phone call inquiry, word of mouth referral, and to drive traffic to the (Corvel Press) web site.

The objective is to develop a post card template with clear and consistent brand imaging, but also with specific blank areas to be populated with multiple photos of respective properties which are to be uploaded with price and descriptive text - to be changed out with each new property being promoted for sale.

Bramble Arc Holdings, Inc. is an online and direct mail marketing service promoting available home buyer opportunities. The objective with each post card mailing is to capture lead contact information, and to promote the Bramble Arc Holdings brand. It is not important to promote any individual personality or person involved with Bramble Arc. Prospective buyer responses from the post card will be directed either to the dedicated web site, and/or to a dedicated customer service phone number. Both the URL and the dedicated phone # are to be highlighted on the post card.

In addition to specific properties for sale (photos and brief text on the front of card), an important function of the post card will be to promote various home buyer services (illustrated on the back of the card). Those various illustrated services are provided by an affiliated team of experienced professionals. The services are enumerated in the pencil concept draft attached with this application. Specifically those services are: Home Buyer Financing, Renovation Design Services, Project Cost Estimates, Rental Property Management, Professional CPA Consultation. Many of those services may be provided free of charge for qualified buyers.

Project Deadline Extended
Reason: I realize that the initial 3 day deadline is not realistic.

Target Market(s)

Real Estate Investors, Rehabbers, Landlords and First Time Home Buyers ...normally male, age 25-50 yr old.

Industry/Entity Type

Residential

Requirements
Must have
• 1. Ability to use basic template style for multiple property photo and text files.
2. A clear call to action and reference to dedicated web site URL and dedicated phone #.
3. Logo/branding to be consistent with web site and other promotional materials. i.e., business card, stationary, other template Bramble Arc post cards targeted to other niche markets.
Nice to have
• "Equity gain - opportunity - renovation" theme/background.

Clear distinct colors and photo images.

Trustworthy, reliable, professional look.
Should not have
• Casual/informal appearance.

Cluttered/overly detailed appearance.

```html
<!DOCTYPE html>
<html lang="en">
<head>
<meta charset="utf-8">
<title>Bramble Arc Holdings — Postcard Template</title>
<link href="https://fonts.googleapis.com/css2?family=Arimo:wght@400&display=swap" rel="stylesheet">
<style>
  :root{
    --lime:#c8d96a; --green:#2e9a4e; --teal:#0f6b4a; --leaf:#6cc06a;
    --olive-lime:#a4c23c; --mint:#3fb36a; --olive:#7f9a3a; --forest:#1b7a45;
    --panel:#e7efd0; --headline:#b9d152; --bar:#c3d86a; --ink:#111; --rule:#b9d152;
  }
  *{margin:0;padding:0;box-sizing:border-box}
  html,body{width:752px;height:1200px;overflow:hidden;background:#fff}
  body{font-family:"Arimo",Arial,sans-serif}
  .postcard{position:relative;width:752px;height:1200px}
  .photo-slot{position:absolute}
  .photo-slot.sky{background:linear-gradient(180deg,#7fb0e0 0%,#b9d3ea 35%,#b08a6e 55%,#5f8a3c 80%,#4f7c31 100%)}
  .photo-slot.porch{background:linear-gradient(180deg,#5d9ae0 0%,#a9cbef 30%,#8a8c8a 55%,#5a8c35 78%,#c9c9c2 100%)}
  .mosaic{position:absolute;display:block}
  .a{fill:var(--lime)} .b{fill:var(--green)} .c{fill:var(--teal)} .d{fill:var(--leaf)}
  .e{fill:var(--olive-lime)} .f{fill:var(--mint)} .g{fill:var(--olive)} .h{fill:var(--forest)}
  .w{fill:#fff}
  .front-panel{position:absolute;left:0;top:301px;width:217px;height:284px;background:var(--panel)}
  .headline{position:absolute;color:var(--headline);font-weight:400;font-size:70px;line-height:68px;letter-spacing:-1px;transform:scaleX(1.25);transform-origin:left top;white-space:nowrap}
  .front-panel .headline{left:29px;top:44px}
  .back-card{position:absolute;left:0;top:602px;width:359px;height:593px}
  .back-card .headline{left:74px;top:146px}
  .cta-bar{position:absolute;left:0;top:491px;width:319px;height:60px;background:var(--bar);padding:7px 0 0 16px;font-size:18px;line-height:1.2;color:var(--ink)}
  .stamp-box{position:absolute;left:585px;top:633px;width:137px;height:139px;background:var(--bar)}
  .address-line{position:absolute;left:397px;width:293px;height:1.5px;background:var(--rule)}
</style>
</head>
<body>
<main class="postcard">

  <!-- Front -->
  <div class="photo-slot sky" style="left:0;top:0;width:185px;height:130px" role="img" aria-label="Property photo: two-storey house with landscaped front lawn"></div>
  <div class="photo-slot sky" style="left:0;top:130px;width:185px;height:171px" role="img" aria-label="Property photo: brick house with gabled roof"></div>
  <div class="photo-slot sky" style="left:185px;top:0;width:441px;height:301px" role="img" aria-label="Main property photo: brick two-storey home with garage and driveway"></div>

  <svg class="mosaic" style="left:626px;top:0" width="126" height="301" viewBox="0 0 3 7" preserveAspectRatio="none" aria-hidden="true">
    <rect class="a" x="0" y="0" width="1" height="1"/><rect class="b" x="1" y="0" width="1" height="1"/><rect class="f" x="2" y="0" width="1" height="1"/>
    <rect class="c" x="0" y="1" width="1" height="1"/><rect class="d" x="1" y="1" width="1" height="1"/><rect class="g" x="2" y="1" width="1" height="1"/>
    <rect class="e" x="0" y="2" width="1" height="1"/><rect class="c" x="1" y="2" width="1" height="1"/><rect class="b" x="2" y="2" width="1" height="1"/>
    <rect class="d" x="0" y="3" width="1" height="1"/><rect class="a" x="1" y="3" width="1" height="1"/><rect class="f" x="2" y="3" width="1" height="1"/>
    <rect class="h" x="0" y="4" width="1" height="1"/><rect class="f" x="1" y="4" width="1" height="1"/><rect class="b" x="2" y="4" width="1" height="1"/>
    <rect class="e" x="0" y="5" width="1" height="1"/><rect class="c" x="1" y="5" width="1" height="1"/><rect class="d" x="2" y="5" width="1" height="1"/>
    <rect class="c" x="0" y="6" width="1" height="1"/><rect class="d" x="1" y="6" width="1" height="1"/><rect class="g" x="2" y="6" width="1" height="1"/>
  </svg>

  <div class="front-panel">
    <p class="headline">text<br>here</p>
  </div>

  <svg class="mosaic" style="left:217px;top:301px" width="126" height="284" viewBox="0 0 3 7" preserveAspectRatio="none" aria-hidden="true">
    <rect class="g" x="0" y="0" width="1" height="1"/><rect class="d" x="1" y="0" width="1" height="1"/><rect class="c" x="2" y="0" width="1" height="1"/>
    <rect class="b" x="0" y="1" width="1" height="1"/><rect class="c" x="1" y="1" width="1" height="1"/><rect class="e" x="2" y="1" width="1" height="1"/>
    <rect class="h" x="0" y="2" width="1" height="1"/><rect class="f" x="1" y="2" width="1" height="1"/><rect class="c" x="2" y="2" width="1" height="1"/>
    <rect class="f" x="0" y="3" width="1" height="1"/><rect class="a" x="1" y="3" width="1" height="1"/><rect class="d" x="2" y="3" width="1" height="1"/>
    <rect class="b" x="0" y="4" width="1" height="1"/><rect class="c" x="1" y="4" width="1" height="1"/><rect class="e" x="2" y="4" width="1" height="1"/>
    <rect class="g" x="0" y="5" width="1" height="1"/><rect class="d" x="1" y="5" width="1" height="1"/><rect class="c" x="2" y="5" width="1" height="1"/>
    <rect class="f" x="0" y="6" width="1" height="1"/><rect class="b" x="1" y="6" width="1" height="1"/><rect class="a" x="2" y="6" width="1" height="1"/>
  </svg>

  <div class="photo-slot porch" style="left:343px;top:301px;width:409px;height:284px" role="img" aria-label="Property photo: grey bungalow with white porch and front walkway"></div>

  <!-- Back -->
  <section class="back-card">
    <svg class="mosaic" style="left:0;top:0" width="359" height="593" viewBox="0 0 9 15" preserveAspectRatio="none" aria-hidden="true">
      <rect class="w" x="0" y="0" width="9" height="15"/>
      <rect class="d" x="0" y="0" width="1" height="1"/><rect class="c" x="1" y="0" width="1" height="1"/><rect class="e" x="2" y="0" width="1" height="1"/><rect class="h" x="3" y="0" width="1" height="1"/><rect class="d" x="4" y="0" width="1" height="1"/><rect class="e" x="5" y="0" width="1" height="1"/><rect class="c" x="6" y="0" width="1" height="1"/><rect class="a" x="7" y="0" width="1" height="1"/><rect class="d" x="8" y="0" width="1" height="1"/>
      <rect class="c" x="0" y="1" width="1" height="1"/><rect class="a" x="0" y="2" width="1" height="1"/><rect class="f" x="0" y="3" width="1" height="1"/><rect class="c" x="0" y="4" width="1" height="1"/><rect class="d" x="0" y="5" width="1" height="1"/><rect class="b" x="0" y="6" width="1" height="1"/><rect class="d" x="0" y="7" width="1" height="1"/><rect class="c" x="0" y="8" width="1" height="1"/><rect class="a" x="0" y="9" width="1" height="1"/><rect class="f" x="0" y="10" width="1" height="1"/><rect class="c" x="0" y="11" width="1" height="1"/><rect class="b" x="0" y="12" width="1" height="1"/><rect class="d" x="0" y="13" width="1" height="1"/>
      <rect class="c" x="8" y="1" width="1" height="1"/><rect class="f" x="8" y="2" width="1" height="1"/><rect class="a" x="8" y="3" width="1" height="1"/><rect class="c" x="8" y="4" width="1" height="1"/><rect class="d" x="8" y="5" width="1" height="1"/><rect class="b" x="8" y="6" width="1" height="1"/><rect class="a" x="8" y="7" width="1" height="1"/><rect class="c" x="8" y="8" width="1" height="1"/><rect class="f" x="8" y="9" width="1" height="1"/><rect class="a" x="8" y="10" width="1" height="1"/><rect class="c" x="8" y="11" width="1" height="1"/><rect class="d" x="8" y="12" width="1" height="1"/><rect class="b" x="8" y="13" width="1" height="1"/>
      <rect class="b" x="0" y="14" width="1" height="1"/><rect class="e" x="1" y="14" width="1" height="1"/><rect class="h" x="2" y="14" width="1" height="1"/><rect class="d" x="3" y="14" width="1" height="1"/><rect class="e" x="4" y="14" width="1" height="1"/><rect class="c" x="5" y="14" width="1" height="1"/><rect class="a" x="6" y="14" width="1" height="1"/><rect class="b" x="7" y="14" width="1" height="1"/><rect class="h" x="8" y="14" width="1" height="1"/>
    </svg>
    <p class="headline">text<br>here</p>
    <p class="cta-bar">visit our website<br>or call</p>
  </section>

  <div class="stamp-box" aria-hidden="true"></div>
  <div class="address-line" style="top:900px"></div>
  <div class="address-line" style="top:932px"></div>
  <div class="address-line" style="top:964px"></div>

</main>
</body>
</html>
```